New Company Business Card Design

I have a new company logo and I want a new business card design. I dont know if the logo file i attached is in the correct format or quality. We are a New York City Specialty construction Firm specializing in high risk out of the box projects. I want a simple and classy business card that people will his card is as crisp as the work his company does.

Target Market(s)

Clients in the heavy construction industry in New York City

Industry/Entity Type

Construction Company

Contact Information for Business Card

Simple Classy - DIFFERENT

Font styles to use
Other font styles liked:
• Mach the logo font in some way

Colors

Designer to choose colors to be used in the design.

Requirements
Must have
• Uniqueness
Nice to have
• Nothing particular - Just different and classy - Timeless
Should not have
• Goofy Shit or Gimmicky shit

```html
<!DOCTYPE html>
<html lang="en">
<head>
<meta charset="utf-8">
<title>Kestrel Build Group — Business Card</title>
<link rel="stylesheet" href="https://fonts.googleapis.com/css2?family=Open+Sans:ital,wght@0,400;0,600;0,800;1,400&display=swap">
<style>
  :root {
    --page: #e9e7e4;
    --card-white: #ffffff;
    --card-dark: #2f2d2e;
    --brand-blue: #2a8fd3;
    --ink: #3a3a3c;
    --ink-soft: #6b6b6e;
    --band-dark: #3b3a3c;
  }
  * { box-sizing: border-box; margin: 0; padding: 0; }
  html, body {
    width: 1200px; height: 1200px; overflow: hidden;
    background: var(--page);
    font-family: "Open Sans", Arial, sans-serif;
  }
  .canvas { position: relative; width: 1200px; height: 1200px; }
  .card {
    position: absolute; left: 170px; width: 860px; height: 491px;
    box-shadow: 0 6px 18px rgba(0,0,0,.12);
    overflow: hidden;
  }
  .card--front { top: 70px; background: var(--card-white); }
  .card--back { top: 640px; background: var(--card-dark); }

  .wordmark {
    font-weight: 800; color: var(--brand-blue);
    letter-spacing: 1px; text-transform: uppercase; line-height: 1;
  }
  .card--front .wordmark {
    position: absolute; left: 60px; top: 62px; font-size: 34px;
  }
  .card--front .wordmark span { display: block; }

  .person { position: absolute; left: 470px; top: 170px; }
  .person__name { font-size: 30px; font-weight: 600; color: var(--ink); }
  .person__role { font-size: 15px; font-style: italic; color: var(--ink-soft); margin-top: 2px; }

  .contact {
    position: absolute; left: 470px; top: 255px;
    font-size: 17px; line-height: 26px; color: var(--ink);
  }
  .contact .label { color: var(--brand-blue); }
  .contact .web { color: var(--brand-blue); }

  .band { position: absolute; }
  .band--blue { left: 0; top: 372px; width: 300px; height: 24px; background: var(--brand-blue); }
  .band--dark { left: 318px; top: 400px; width: 542px; height: 46px; background: var(--band-dark); }

  .card--back .wordmark {
    position: absolute; left: 0; right: 0; top: 50%;
    transform: translateY(-50%);
    text-align: center; font-size: 46px;
  }
</style>
</head>
<body>
<main class="canvas">
  <section class="card card--front" aria-label="Business card front">
    <div class="wordmark"><span>Kestrel</span><span>Build Group</span></div>

    <div class="person">
      <p class="person__name">John Doe</p>
      <p class="person__role">Director</p>
    </div>

    <div class="contact">
      <p><span class="label">M :</span> 1-234-567890</p>
      <p><span class="label">E :</span> john@kestrelbuild.com</p>
      <p><span class="label">T :</span> 123.456.7890 &nbsp;<span class="label">F :</span> 000.000.0000</p>
      <p>Dummy city, Dummy Country Land</p>
      <p class="web">www.kestrelbuild.com</p>
    </div>

    <div class="band band--blue"></div>
    <div class="band band--dark"></div>
  </section>

  <section class="card card--back" aria-label="Business card back">
    <div class="wordmark">Kestrel Build Group</div>
  </section>
</main>
</body>
</html>
```